Visitenkarten-Design für Pflegedienst
Zielgruppe
Pflegedienst
Aufgabenstellung
Siehe Beispielvisitenkarte. Es soll so ähnlich designt werden mit hochwertigem Papier. Die Angaben darauf sind auch schon korrekt.

```html
<!DOCTYPE html>
<html lang="de">
<head>
<meta charset="utf-8">
<title>Visitenkarte Atemwerk12 GmbH</title>
<link href="https://fonts.googleapis.com/css2?family=Montserrat:wght@300;400;500&display=swap" rel="stylesheet">
<style>
  :root {
    --backdrop: #dadada;
    --paper: #ffffff;
    --brand-blue: #33568a;
    --brand-red: #d31216;
    --ink: #1a1a1a;
    --photo-tone-a: #f2f2f2;
    --photo-tone-b: #c9b7a8;
  }
  * { margin: 0; padding: 0; box-sizing: border-box; }
  html, body { width: 1200px; height: 885px; overflow: hidden; }
  body {
    background: var(--backdrop);
    font-family: "Montserrat", sans-serif;
    color: var(--ink);
    position: relative;
  }
  .card {
    position: absolute;
    top: 303px;
    width: 432px;
    height: 280px;
    overflow: hidden;
  }
  .card--front { left: 103px; background: var(--paper); }
  .card--back { left: 656px; background: var(--brand-blue); }

  .line { position: absolute; left: 40px; white-space: nowrap; font-size: 12.5px; line-height: 1; }
  .icon { position: absolute; left: 18px; width: 12px; height: 12px; }

  .person-name { font-size: 14.8px; font-weight: 400; letter-spacing: 0.2px; top: 55px; }
  .person-role { font-size: 10.8px; top: 76px; }
  .company { font-weight: 500; top: 126px; }
  .addr-1 { top: 141px; }
  .addr-2 { top: 156px; }
  .mobile { top: 187px; }
  .phone { top: 202px; }
  .fax { top: 217px; }
  .email { top: 232px; }

  .portrait {
    position: absolute;
    left: 257px;
    top: 64px;
    width: 152px;
    height: 152px;
    border-radius: 50%;
    border: 3.5px solid var(--brand-blue);
    background: radial-gradient(circle at 50% 55%, var(--photo-tone-b) 0%, var(--photo-tone-a) 62%);
  }
  .front-bands, .back-base { position: absolute; left: 0; bottom: 0; }

  .brand {
    position: absolute;
    left: 0; right: 0;
    top: 118px;
    display: flex;
    justify-content: center;
    align-items: center;
    gap: 12px;
  }
  .brand-dot { width: 22px; height: 22px; border-radius: 50%; background: var(--brand-red); }
  .brand-name { color: var(--paper); font-size: 27px; font-weight: 300; letter-spacing: 0.5px; }
  .website {
    position: absolute;
    left: 118px; width: 198px;
    top: 240px;
    text-align: center;
    color: var(--paper);
    font-size: 14px;
  }
</style>
</head>
<body>

<section class="card card--front">
  <svg class="icon" style="top:55px" viewBox="0 0 12 12"><circle cx="6" cy="6" r="6" fill="var(--brand-blue)"/><circle cx="6" cy="4.6" r="2" fill="#fff"/><path d="M2.6 9.6a3.6 3 0 0 1 6.8 0z" fill="#fff"/></svg>
  <p class="line person-name">JONAS WEBERLING LL.M.</p>
  <p class="line person-role">Wirtschaftsjurist - Geschäftsführer</p>

  <p class="line company">Atemwerk12 GmbH</p>
  <svg class="icon" style="top:142px" viewBox="0 0 12 12"><path d="M6 0.5a4.3 4.3 0 0 1 4.3 4.3C10.3 8 6 11.5 6 11.5S1.7 8 1.7 4.8A4.3 4.3 0 0 1 6 .5z" fill="var(--brand-blue)"/><circle cx="6" cy="4.8" r="1.6" fill="#fff"/></svg>
  <p class="line addr-1">Lindenhofer Str. 18</p>
  <p class="line addr-2">71034 Böblingen</p>

  <svg class="icon" style="top:187px" viewBox="0 0 12 12"><circle cx="6" cy="6" r="6" fill="var(--brand-blue)"/><rect x="4" y="2.5" width="4" height="7" rx="0.8" fill="#fff"/></svg>
  <p class="line mobile">+49 151 40213398</p>
  <svg class="icon" style="top:202px" viewBox="0 0 12 12"><circle cx="6" cy="6" r="6" fill="var(--brand-blue)"/><path d="M3.6 3c.5-.4 1-.4 1.2 0l.6 1.2c.2.4 0 .7-.3.9-.2.2 0 .8.6 1.4s1.2.8 1.4.6c.2-.3.5-.5.9-.3L9 7.4c.4.2.4.7 0 1.1-1 1-3 .3-4.3-1S2.6 4 3.6 3z" fill="#fff"/></svg>
  <p class="line phone">+49 7031 4829500</p>
  <svg class="icon" style="top:217px" viewBox="0 0 12 12"><circle cx="6" cy="6" r="6" fill="var(--brand-blue)"/><rect x="3" y="5" width="6" height="3.5" rx="0.6" fill="#fff"/><rect x="4" y="3" width="4" height="2" fill="#fff"/></svg>
  <p class="line fax">+49 7031 4829502</p>
  <svg class="icon" style="top:232px" viewBox="0 0 12 12"><circle cx="6" cy="6" r="6" fill="var(--brand-blue)"/><rect x="3" y="4" width="6" height="4.2" rx="0.6" fill="#fff"/><path d="M3.2 4.3 6 6.3l2.8-2" stroke="var(--brand-blue)" stroke-width="0.8" fill="none"/></svg>
  <p class="line email">jw@atemwerk12.de</p>

  <div class="portrait" role="img" aria-label="Porträtfoto des Geschäftsführers"></div>

  <svg class="front-bands" width="432" height="22" viewBox="0 0 432 22">
    <polygon points="0,9 250,9 238,22 0,22" fill="var(--brand-red)"/>
    <polygon points="266,0 432,0 432,22 246,22" fill="var(--brand-blue)"/>
  </svg>
</section>

<section class="card card--back">
  <div class="brand">
    <span class="brand-dot"></span>
    <span class="brand-name">ATEMWERK12 GMBH</span>
  </div>

  <svg class="back-base" width="432" height="60" viewBox="0 0 432 60">
    <path d="M0,35 H106 Q118,35 118,24 V16 Q118,0 134,0 H300 Q316,0 316,16 V24 Q316,35 328,35 H432 V60 H0 Z" fill="var(--brand-red)"/>
  </svg>
  <p class="website">www.atemwerk12.de</p>
</section>

</body>
</html>
```